Manufacturing business needs a website revamp

We are a manufacturing business supplying parts and modules to mid-high end consumer electronics brands from kitchen appliances to powered tools mainly in US/Europe. We want design ideas for a revamp of our website. We're aiming for a look and feel that's sleek, tidy and modern whilst still providing the right balance for content. A smooth and comfortable user experience that directs users to the information they may be looking for and promote our services. Something that incorporates design ideas such as: responsive design, lazy loading, slider banners, responsive layout, dynamic scrolling, liquid layout, full page headers etc... These are just terms bounced around within our team and certainly neither exclusive nor absolutely necessary. This is our current website for reference: https://www.varlumotek.com/ , which we feel is both outdated and doesn't engage visitors.

Attached is our planned new site map (we’re open to additional ideas here). We would like mock ups for each page on the site map. We will subsequently fill out the contents ourselves, but require design directions on e.g. how much text should go at which spot. E.g. for our Automotive page under Industries, we would like a suitable layout to be designed, as well as designated areas for texts. As for assets, please use any of the assets already on our current site or external source. We’ve yet to finalize on our selection of assets so please use the above as placeholders for now. Additionally, we would want a mock up for a pop-up frame to showcase additional technical specifications for some of our product ranges. For example, under the powertools section of our current website, we have additional listings under our product range. Currently they do not have a pop up function, but if we were to create a pop up frame to display detailed specifications, what layout should we use?

Finally, our target audiences are professional representatives from leading consumer brands who may be interested in our services. Our target customers are mid-high end brands. Think, for example, KVR/Harwick for automotive, Frostivane/Trell/Dovarin for consumer electronics/kitchen appliances, and Pelham Grove & Tasker/Brantover for powered tools. Typically it will be their product designers/engineers and supply chain representatives who will visit our website.

Target Market(s)

Professional product engineers/designers from mid-high end consumer electronics brands.

Industry/Entity Type

Manufacturing

Contact Information for Business Card

Attached are back and front of our current name card design. Again, we're open to changes that matches the style of our future website design. A few notes on the business card design:
- Cannot have blue background
- Does not have to be bilingual. I.e. open to single language design on one side and logo on the other

Coding

Coded - Design and coding required

Number of Pages Required

5+ page

Font styles to use
Sans Serif

Colors
3176b5

Requirements
Must have
• Color scheme must be based on the blue from our current website design. We will be keeping our current logo, hence must match that logo.
Nice to have
• Plim (or similar platforms) as demos/final solutions ok.
Should not have
• See brief

```html
<!DOCTYPE html>
<html lang="en">
<head>
<meta charset="utf-8">
<title>Varlumo — Powering You Up For Success</title>
<link href="https://fonts.googleapis.com/css2?family=Bebas+Neue&family=Poppins:wght@300;400;500;600&display=swap" rel="stylesheet">
<style>
:root{
  --blue:#3b9de4;
  --blue-dark:#1b4f86;
  --ink:#111418;
  --text:#555b62;
  --muted:#8a9097;
  --soft:#f7f7f7;
  --line:#ececec;
  --white:#ffffff;
  --black:#0c0d0f;
}
*{box-sizing:border-box;margin:0;padding:0}
html,body{width:1200px;height:3172px;overflow:hidden}
body{position:relative;font-family:"Poppins",sans-serif;color:var(--text);background:var(--white)}
.abs{position:absolute}
a{color:inherit;text-decoration:none}

/* top bar */
.topbar{left:0;top:0;width:1200px;height:37px;background:var(--blue);color:var(--white);font-size:13px}
.topbar .cell{position:absolute;top:0;height:37px;display:flex;align-items:center;gap:10px;border-left:1px solid rgba(255,255,255,.35)}
.topbar .phone{left:765px;width:146px;padding-left:16px}
.topbar .lang{left:911px;width:128px;padding-left:20px;border-right:1px solid rgba(255,255,255,.35);font-size:12px}

/* header */
.header{left:0;top:37px;width:1200px;height:75px;background:var(--white)}
.brand{display:flex;align-items:center;gap:10px}
.brand .mark{width:30px;height:30px;background:var(--blue)}
.brand .name{font-weight:600;font-size:27px;color:var(--ink);line-height:1}
.header .brand{position:absolute;left:161px;top:20px}
.nav{position:absolute;top:0;height:75px;display:flex;align-items:center;font-size:12px;color:#6b7178}
.nav a{position:absolute;white-space:nowrap}
.nav a.active{color:var(--blue)}

/* hero */
.hero{left:0;top:112px;width:1200px;height:638px;background:linear-gradient(100deg,#2a2c2b 0%,#4b4c48 40%,#6a6a63 60%,#3a3b38 100%)}
.hero-title{left:162px;top:250px;font-family:"Bebas Neue",sans-serif;font-weight:400;font-size:64px;line-height:63px;color:var(--white);text-transform:uppercase}
.hero-title .accent{color:var(--blue)}
.hero-text{left:162px;top:454px;width:390px;font-size:13px;line-height:22.5px;color:var(--white)}

/* button */
.btn{position:absolute;height:45px;display:flex;align-items:center;justify-content:center;color:var(--white);font-size:13px;font-weight:500;text-transform:uppercase;background:var(--blue);clip-path:polygon(8px 0,100% 0,calc(100% - 8px) 100%,0 100%)}
.btn::before{content:"";position:absolute;left:0;top:0;width:12px;height:100%;background:var(--blue-dark);clip-path:polygon(8px 0,12px 0,4px 100%,0 100%)}
.btn.small{height:36px;font-size:11px}

/* sections */
.section-mark{left:583px;top:818px;width:34px;height:34px;background:var(--blue)}
.h2{font-weight:600;font-size:33px;color:var(--ink);letter-spacing:-.3px;white-space:nowrap}
.h2 .accent{color:var(--blue);font-weight:500}
.center{left:0;width:1200px;text-align:center}
.lead{font-size:11px;line-height:19px;color:var(--muted)}

.services{left:0;top:1199px;width:1200px;height:650px;background:var(--soft)}
.card{position:absolute;top:1387px;width:270px;height:413px;background:var(--white);border:1px solid var(--line)}
.card .photo{position:absolute;left:0;top:0;width:268px;height:180px}
.card .photo-cut{position:absolute;right:0;top:165px;width:68px;height:15px;background:var(--white);clip-path:polygon(15px 0,100% 0,100% 100%,0 100%)}
.card h3{position:absolute;left:23px;top:208px;font-weight:500;font-size:17px;color:var(--ink)}
.card p{position:absolute;left:23px;top:253px;width:230px;font-size:10.5px;line-height:18.7px;color:var(--muted)}
.card .btn{left:23px;top:338px;width:107px}

.core{left:0;top:1846px;width:1200px;height:507px;background:linear-gradient(100deg,#0a1420 0%,#1a2a3d 45%,#3a5672 65%,#1d2c40 100%);clip-path:polygon(0 0,50% 40px,100% 0,100% 100%,50% 458px,0 100%)}
.core-title{left:162px;top:1945px;color:var(--white)}
.core-title .accent{color:var(--blue);font-weight:500}
.core-text{left:162px;top:2007px;width:390px;font-size:12.5px;line-height:21px;color:var(--white)}
.core-list{left:162px;top:2068px;list-style:none;color:var(--white);font-size:15.5px}
.core-list li{display:flex;align-items:center;gap:14px;height:30.3px}

.news-card{position:absolute;top:2434px;width:270px}
.news-card .photo{width:270px;height:179px}
.news-card .date{position:absolute;left:4px;top:6px;height:27px;padding:0 12px;min-width:110px;background:var(--blue);color:var(--white);font-size:11px;display:flex;align-items:center;justify-content:center}
.news-card h4{margin-top:22px;font-weight:400;font-size:12.5px;line-height:22px;color:var(--ink);padding-left:2px}

/* footer */
.footer{left:0;top:2843px;width:1200px;height:329px;background:var(--black)}
.footer .panel{position:absolute;left:0;top:0;width:463px;height:329px;background:var(--blue);clip-path:polygon(0 0,463px 0,345px 100%,0 100%)}
.footer-brand{left:161px;top:2918px}
.footer-brand .mark{background:var(--white);width:34px;height:34px}
.footer-brand .name{color:var(--white);font-size:31px}
.social{position:absolute;top:2987px;width:36px;height:36px;border-radius:50%;background:var(--white);color:var(--black);font-size:12px;font-weight:600;display:flex;align-items:center;justify-content:center}
.copyright{left:162px;top:3057px;width:190px;font-size:11.5px;line-height:21px;color:var(--white)}
.fcol h5{font-weight:500;font-size:18px;color:var(--blue);margin-bottom:12px}
.fcol ul{list-style:none;font-size:11.5px;color:var(--white);line-height:22.5px}
.addr{font-size:11.5px;line-height:21px;color:var(--white);display:flex;gap:16px}
.addr svg{flex:none;margin-top:3px}
</style>
</head>
<body>

<!-- top bar -->
<div class="abs topbar">
  <div class="cell phone">
    <svg width="16" height="16" viewBox="0 0 24 24" fill="none" stroke="#fff" stroke-width="2"><path d="M22 16.9v3a2 2 0 0 1-2.2 2 19.8 19.8 0 0 1-8.6-3.1 19.5 19.5 0 0 1-6-6A19.8 19.8 0 0 1 2.1 4.2 2 2 0 0 1 4.1 2h3a2 2 0 0 1 2 1.7c.1 1 .4 1.9.7 2.8a2 2 0 0 1-.5 2.1L8 9.9a16 16 0 0 0 6 6l1.3-1.3a2 2 0 0 1 2.1-.4c.9.3 1.8.6 2.8.7a2 2 0 0 1 1.7 2z"/></svg>
    <span>123.555.0188</span>
  </div>
  <div class="cell lang">
    <span>Languages</span>
    <svg width="17" height="17" viewBox="0 0 24 24" fill="none" stroke="#fff" stroke-width="2"><circle cx="12" cy="12" r="10"/><path d="M2 12h20M12 2a15 15 0 0 1 0 20M12 2a15 15 0 0 0 0 20"/></svg>
  </div>
</div>

<!-- header -->
<header class="abs header">
  <div class="brand"><span class="mark"></span><span class="name">Varlumo</span></div>
  <nav class="nav">
    <a class="active" style="left:515px">Home</a>
    <a style="left:575px">About Us</a>
    <a style="left:653px">Industries</a>
    <a style="left:736px">Core Competencies</a>
    <a style="left:878px">News</a>
    <a style="left:935px">Contact Us</a>
    <svg style="position:absolute;left:1023px;top:29px" width="16" height="16" viewBox="0 0 24 24" fill="none" stroke="#222" stroke-width="2.2"><circle cx="10" cy="10" r="7"/><path d="M15 15l6 6"/></svg>
  </nav>
</header>

<!-- hero -->
<section class="abs hero" role="img" aria-label="Close-up photograph of an industrial stamping press in a factory"></section>
<h1 class="abs hero-title"><span class="accent">Varlumo</span><br>Powering you up<br>for success</h1>
<p class="abs hero-text">Our parent company was founded in 1978 as a switch manufacturer in Hong Kong, the Varlumo brand has achieved global recognition in various sectors.</p>
<a class="btn" style="left:161px;top:548px;width:135px">Learn More</a>

<!-- about -->
<span class="abs section-mark" aria-hidden="true"></span>
<h2 class="abs center h2" style="top:892px">About <span class="accent">Company</span></h2>
<p class="abs center lead" style="top:956px">Our parent company was founded in 1978 as a switch manufacturer in Hong Kong, the<br>Varlumo brand has achieved global recognition in various sectors.</p>
<p class="abs center lead" style="top:1009px">Over four decades later, we continue to facilitate our customers' innovation and production<br>across the world with a wide range of integration solutions, enabling our customers to keep<br>ahead of the competition.</p>
<a class="btn" style="left:532px;top:1095px;width:135px">Learn More</a>

<!-- what we do -->
<section class="abs services"></section>
<h2 class="abs center h2" style="top:1252px">What We <span class="accent">Do</span></h2>
<p class="abs center" style="top:1310px;font-size:12.5px;line-height:20px;color:var(--text)">Our commitment to your success is our drive to continuous<br>innovation and improvement.</p>

<article class="card" style="left:161px">
  <div class="photo" role="img" aria-label="Hand holding a car key fob beside a white car" style="background:linear-gradient(120deg,#c9ccd0,#8e949b 60%,#5a5f66)"></div>
  <div class="photo-cut"></div>
  <h3>Automotive</h3>
  <p>Combining Varlumo's decades of experien -ce, Kestrel Automotive produces the highest quality components for world's top automotive brands.</p>
  <a class="btn small">Learn More</a>
</article>
<article class="card" style="left:464px">
  <div class="photo" role="img" aria-label="Woman operating a smart built-in oven with her phone" style="background:linear-gradient(120deg,#2d2b2a,#5b4a40 55%,#c9a98a)"></div>
  <div class="photo-cut"></div>
  <h3>Home Appliances</h3>
  <p>Varlumo components have been widely adopted by the most trusted brands in home appliances, automotive, power tools and many other sectors.</p>
  <a class="btn small">Learn More</a>
</article>
<article class="card" style="left:769px">
  <div class="photo" role="img" aria-label="Industrial printing machine nozzle in a blue-toned workshop" style="background:linear-gradient(120deg,#1f3a5a,#6d88a6 55%,#c8cfd6)"></div>
  <div class="photo-cut"></div>
  <h3>Power Tools</h3>
  <p>Being the leading supplier of power tool switches and integrated electronic con trol modules, Varlumo has been trusted by the top international brands.</p>
  <a class="btn small">Learn More</a>
</article>

<!-- core competencies -->
<section class="abs core" role="img" aria-label="Engineer holding a tablet showing production dashboards"></section>
<h2 class="abs h2 core-title">Core <span class="accent">Competencies</span></h2>
<p class="abs core-text">Our commitment to your success is our drive to continuous innovation and improvement.</p>
<ul class="abs core-list">
  <li><svg width="16" height="16" viewBox="0 0 16 16"><path d="M8 0l3 3-3 3-3-3zM3 5l3 3-3 3-3-3zM13 5l3 3-3 3-3-3zM8 10l3 3-3 3-3-3z" fill="#3b9de4"/></svg>Awards &amp; Honors</li>
  <li><svg width="16" height="16" viewBox="0 0 16 16"><path d="M8 0l3 3-3 3-3-3zM3 5l3 3-3 3-3-3zM13 5l3 3-3 3-3-3zM8 10l3 3-3 3-3-3z" fill="#3b9de4"/></svg>Research &amp; Development</li>
  <li><svg width="16" height="16" viewBox="0 0 16 16"><path d="M8 0l3 3-3 3-3-3zM3 5l3 3-3 3-3-3zM13 5l3 3-3 3-3-3zM8 10l3 3-3 3-3-3z" fill="#3b9de4"/></svg>Manufacturing Capabilities</li>
  <li><svg width="16" height="16" viewBox="0 0 16 16"><path d="M8 0l3 3-3 3-3-3zM3 5l3 3-3 3-3-3zM13 5l3 3-3 3-3-3zM8 10l3 3-3 3-3-3z" fill="#3b9de4"/></svg>Quality Management</li>
</ul>
<a class="btn" style="left:161px;top:2221px;width:135px">Get a Quote</a>

<!-- news -->
<h2 class="abs center h2" style="top:2356px">Recent News</h2>
<article class="news-card" style="left:161px">
  <div class="photo" role="img" aria-label="Group of visitors touring a factory floor" style="background:linear-gradient(120deg,#b9c2c9,#6f7880 60%,#3d444b)"></div>
  <span class="date">September 2020</span>
  <h4>Riverton Robotics Association visits Varlumo</h4>
</article>
<article class="news-card" style="left:465px">
  <div class="photo" role="img" aria-label="Rows of automated material distribution racks" style="background:linear-gradient(120deg,#d6d8da,#7c8086 55%,#2b2e32)"></div>
  <span class="date">August 2020</span>
  <h4>Varlumo's self-developed Intelligent Material Distribution System granted utility model patent by NPIA</h4>
</article>
<article class="news-card" style="left:769px">
  <div class="photo" role="img" aria-label="Historic red-brick university building under a clear sky" style="background:linear-gradient(180deg,#b7cbe0,#a8745c 55%,#4f5a3c)"></div>
  <span class="date">July 2020</span>
  <h4>Varlumo and academia join forces to drive innovation</h4>
</article>
<a class="btn" style="left:532px;top:2739px;width:135px">View All News</a>

<!-- footer -->
<footer class="abs footer"><div class="panel"></div></footer>
<div class="abs brand footer-brand"><span class="mark"></span><span class="name">Varlumo</span></div>
<span class="social" style="left:162px">f</span>
<span class="social" style="left:207px">t</span>
<span class="social" style="left:252px">in</span>
<p class="abs copyright">Copyright © 2020 Varlumo. All Rights Reserved.</p>

<div class="abs fcol" style="left:485px;top:2901px">
  <h5>Links</h5>
  <ul><li>Home</li><li>About Us</li><li>Industries</li><li>Core Competencies</li><li>News</li><li>Contact Us</li></ul>
</div>
<div class="abs fcol" style="left:680px;top:2901px">
  <h5>Help</h5>
  <ul><li>Languages</li><li>Privacy Policy</li><li>T &amp; cs</li><li>Careers</li></ul>
</div>
<div class="abs fcol" style="left:837px;top:2901px;width:220px">
  <h5>Address</h5>
  <div class="addr"><svg width="14" height="18" viewBox="0 0 14 18"><path d="M7 0a7 7 0 0 0-7 7c0 5 7 11 7 11s7-6 7-11a7 7 0 0 0-7-7z" fill="#3b9de4"/><circle cx="7" cy="7" r="2.5" fill="#0c0d0f"/></svg><span>4/F, Harbourline Industrial Centre, 18 Merrow St., Eastbay</span></div>
  <div class="addr" style="margin-top:12px"><svg width="14" height="14" viewBox="0 0 24 24"><path d="M22 16.9v3a2 2 0 0 1-2.2 2A19.8 19.8 0 0 1 2.1 4.2 2 2 0 0 1 4.1 2h3a2 2 0 0 1 2 1.7c.1 1 .4 1.9.7 2.8a2 2 0 0 1-.5 2.1L8 9.9a16 16 0 0 0 6 6l1.3-1.3a2 2 0 0 1 2.1-.4c.9.3 1.8.6 2.8.7a2 2 0 0 1 1.7 2z" fill="#3b9de4"/></svg><span>Tel&nbsp; :&nbsp; (852) 3041 6620<br>Mo&nbsp; :&nbsp; (852) 9480 1173</span></div>
  <div class="addr" style="margin-top:12px"><svg width="14" height="12" viewBox="0 0 14 12"><rect width="14" height="12" fill="#3b9de4"/><path d="M0 0l7 6 7-6" fill="none" stroke="#0c0d0f" stroke-width="1.4"/></svg><span>lena.marsh@varlumo<br>tek.com</span></div>
</div>

</body>
</html>
```